Varbek - Nutritious Snacks and Desserts

We need a creative e-commerce website in which all features--buttons, background, etc.--convey our message: We sell delicious, nutritious snacks and desserts that most closely comply with the paleo diet guidelines. Our first product is Brunavo®--raw, vegan, paleo chocolate balls that are made of dates, coconut, and cocoa. Our products are organic, raw, irresistible and nutritious. We have several versions of Brunavo® in development, as well as mousse, ice cream, and crackers. Our mission is to purvey basic healthy foods. Our motto is, "Fuel for the Daily Trail-Seeker(tm)."

Target Market(s)

Health-conscious professionals who tend to shop at health food stores. Our products also meet the requirements of a gluten-free diet; and they also don't contain refined sugar, so shoppers with gluten and possibly sugar issues are incidental customers.

Industry/Entity Type

Health Product

Coding

Coded - Design and coding required

Number of Pages Required

5+ page

Colors

Designer to choose colors to be used in the design.

Requirements
Must have
• We need at least a home page, a products page, an about-us page, a contact page, and a shopping cart page. We would like to be able to add products on our own later. We should be able to handle some basic coding, especially if it's just a matter of copying and modifying product pages. We would also like the ability in the future to add blogging pages, allowing us to write articles about health food and healthy lifestyle, thus attracting web-traffic (SEO).
• Other features we would like to have:
• Product photo slider on the hopepage
• Back-to-top button at the bottom of the home page
• Make sure the site is mobile-compatible
• A search bar at the top of the homepage
• "Create an account" and "Previous orders"--allowing customers to see their previous orders and reorder what they purchased in the past.
Nice to have
• We would like to convey the paleo theme without actually stating it anywhere. We'll add text as necessary, according to the page layout; you can use ipsum lorem for purpose of demonstration.

```html
<!DOCTYPE html>
<html lang="en">
<head>
<meta charset="utf-8">
<title>Varbek Foods</title>
<link rel="stylesheet" href="https://fonts.googleapis.com/css2?family=Bitter:wght@400;700&family=Lato:wght@400;700&family=Open+Sans:wght@400&display=swap">
<style>
:root{
  --green:#74c51a;
  --green-dark:#62a913;
  --ink:#333333;
  --text:#444444;
  --muted:#666666;
  --paper:#ffffff;
  --mist:#ededed;
  --footer:#2f2f2f;
}
*{box-sizing:border-box;margin:0;padding:0}
html,body{width:1200px;height:2695px;overflow:hidden}
body{position:relative;background:var(--paper);font-family:'Lato',sans-serif;color:var(--text)}
.abs{position:absolute}

/* header */
.site-header{left:0;top:0;width:1200px;height:161px;background:var(--paper)}
.brand{left:80px;top:40px;display:flex;align-items:center;gap:14px}
.brand-dot{width:60px;height:60px;border-radius:50%;background:var(--green)}
.brand-name{font-family:'Lato',sans-serif;font-weight:700;font-size:44px;color:var(--green);letter-spacing:3px}
.cart-btn{left:985px;top:27px;width:172px;height:48px;display:flex;border-radius:3px;overflow:hidden}
.cart-label{flex:1;background:var(--green);color:#3d5a12;font-size:19px;font-weight:700;display:flex;align-items:center;justify-content:center}
.cart-icon{width:54px;background:#555;display:flex;align-items:center;justify-content:center}
.main-nav{right:45px;top:110px;display:flex;gap:40px;font-size:17px;color:#444;text-transform:uppercase}
.main-nav .active{color:var(--green)}

/* hero */
.hero{left:0;top:161px;width:1200px;height:579px;background:linear-gradient(100deg,#6b5a3a 0%,#b38b4a 30%,#c9a25a 55%,#7a9a3a 75%,#3d4a2a 100%)}
.hero-panel{left:80px;top:161px;width:430px;height:579px;background:rgba(116,197,26,.85);text-align:center}
.hero-title{position:absolute;left:0;top:160px;width:430px;font-family:'Bitter',serif;font-weight:700;font-size:40px;line-height:60px;color:#fff}
.hero-btn{position:absolute;left:114px;top:373px;width:179px;height:51px;border:3px solid #fff;outline:2px solid var(--green-dark);background:#fff;color:var(--green);font-weight:700;font-size:21px;display:flex;align-items:center;justify-content:center}
.hero-dots{position:absolute;left:158px;top:500px;display:flex;gap:6px}
.hero-dots span{width:15px;height:15px;border-radius:50%;border:2px solid #fff}
.hero-dots span.on{background:#fff}

/* welcome */
.welcome{left:0;top:740px;width:1200px;height:301px;background:var(--ink);text-align:center;color:#eee}
.welcome h1{margin-top:66px;font-family:'Bitter',serif;font-weight:700;font-size:42px;color:var(--green)}
.welcome p{font-family:'Open Sans',sans-serif;font-size:15.5px;line-height:27px}
.welcome .lead{margin-top:28px}
.welcome .tail{margin-top:18px}

/* products */
.products{left:0;top:1041px;width:1200px;height:537px;background:var(--mist)}
.section-title{font-family:'Bitter',serif;font-weight:700;font-size:42px;color:var(--green);text-align:center;width:1200px;left:0}
.utensil{background:linear-gradient(90deg,#9a9a9a,#f4f4f4 50%,#8a8a8a);border-radius:20px}
.product-card{width:278px;height:330px;background:#fff;padding:6px}
.product-inner{width:100%;height:100%;border:2px solid var(--green);border-radius:4px;overflow:hidden;display:flex;flex-direction:column}
.product-name{height:78px;display:flex;align-items:center;justify-content:center;font-family:'Bitter',serif;font-weight:700;font-size:28px;color:var(--green)}
.product-price{height:46px;background:var(--green);color:#fff;font-family:'Bitter',serif;font-weight:700;font-size:23px;display:flex;align-items:center;justify-content:center}
.product-photo{flex:1}

/* blog */
.blog-card{width:515px;height:193px;border:2px solid var(--green);border-radius:4px;background:#fff}
.blog-photo{position:absolute;left:9px;top:9px;width:225px;height:172px}
.blog-body{position:absolute;left:258px;top:22px;width:240px}
.blog-body h3{font-size:18px;font-weight:700;line-height:29px;color:#333}
.blog-date{font-size:14px;color:#555;margin-top:8px;display:flex;align-items:center;gap:10px}
.blog-body p{font-size:14px;line-height:26px;color:#555;margin-top:4px}

/* contact */
.contact{left:0;top:1985px;width:1200px;height:580px;background:#efefef}
.contact-photo{left:360px;top:2020px;width:800px;height:500px;border-radius:40% 30% 45% 45%/35% 30% 55% 55%;background:radial-gradient(ellipse at 55% 45%,#5a3a2a 0%,#6e4a33 45%,#8a6248 70%,#e9e9e9 100%)}
.contact-card{left:80px;top:2063px;width:514px;height:279px;background:rgba(255,255,255,.82);border-radius:6px;text-align:center}
.contact-card h2{margin-top:40px;font-family:'Bitter',serif;font-weight:700;font-size:40px;color:var(--green)}
.contact-card .c-brand{margin-top:14px;font-weight:700;font-size:17px;color:var(--green)}
.contact-card p{font-family:'Open Sans',sans-serif;font-size:14.5px;color:#555}
.contact-card .c-tag{margin-top:4px}
.contact-card .c-phone{margin-top:26px}
.contact-card .c-mail{margin-top:22px}

/* footer */
.site-footer{left:0;top:2565px;width:1200px;height:130px;background:var(--footer);color:#eee}
.footer-links{position:absolute;left:82px;top:30px;display:flex;gap:45px;font-size:15px}
.footer-social{position:absolute;right:45px;top:28px;display:flex;gap:22px}
.footer-social span{width:18px;height:18px;border-radius:50%;background:#fff}
.copyright{position:absolute;left:0;top:80px;width:1200px;text-align:center;font-size:14.5px}
</style>
</head>
<body>

<header class="site-header abs">
  <div class="brand abs"><span class="brand-dot"></span><span class="brand-name">varbek</span></div>
  <div class="cart-btn abs">
    <span class="cart-label">MY CART</span>
    <span class="cart-icon">
      <svg width="30" height="24" viewBox="0 0 30 24"><path d="M2 9h26l-3 13H5z" fill="none" stroke="#9ed85a" stroke-width="2"/><path d="M9 9l5-7M21 9l-5-7" stroke="#9ed85a" stroke-width="2"/><path d="M10 12v7M15 12v7M20 12v7" stroke="#9ed85a" stroke-width="2"/></svg>
    </span>
  </div>
  <nav class="main-nav abs"><span class="active">Home</span><span>About</span><span>Products</span><span>Blog</span><span>Contact</span></nav>
</header>

<section class="hero abs" role="img" aria-label="Photo of a fresh vegan salad with avocado, mango and sprouts on a white plate"></section>
<div class="hero-panel abs">
  <h2 class="hero-title">Fuel for the Daily<br>Trail-SeekerTM</h2>
  <div class="hero-btn">SHOP NOW</div>
  <div class="hero-dots"><span class="on"></span><span></span><span></span><span></span></div>
</div>

<section class="welcome abs">
  <h1>Welcome to Varbek Foods.</h1>
  <p class="lead">Our products are raw, organic, vegan, gluten-free, dairy-free, fiber-rich, nutrient-dense, antioxidant-rich<br>real foods with no preservatives, no added sugar, and no artificial or plant-based sweeteners.</p>
  <p class="tail">And they are irresistibly scrumptious!</p>
</section>

<section class="products abs"></section>
<h2 class="section-title abs" style="top:1090px">Our products</h2>
<div class="utensil abs" style="left:84px;top:1072px;width:46px;height:480px" role="img" aria-label="Photo of a silver fork"></div>
<div class="utensil abs" style="left:1108px;top:1072px;width:46px;height:480px" role="img" aria-label="Photo of a silver knife"></div>

<div class="product-card abs" style="left:163px;top:1171px"><div class="product-inner">
  <div class="product-name">Brunavo</div><div class="product-price">Starting at $0.00</div>
  <div class="product-photo" role="img" aria-label="Photo of a Brunavo tub" style="background:linear-gradient(135deg,#c9c2b4,#8a6b4a 60%,#5a5650)"></div>
</div></div>
<div class="product-card abs" style="left:478px;top:1171px"><div class="product-inner">
  <div class="product-name">vegan</div><div class="product-price">Starting at $0.00</div>
  <div class="product-photo" role="img" aria-label="Photo of a vegan salad plate" style="background:linear-gradient(135deg,#4a3a2a,#d9a33a 45%,#7aa03a 70%,#e5e0d6)"></div>
</div></div>
<div class="product-card abs" style="left:793px;top:1171px"><div class="product-inner">
  <div class="product-name">chocolate balls</div><div class="product-price">Starting at $0.00</div>
  <div class="product-photo" role="img" aria-label="Photo of chocolate balls on a plate" style="background:linear-gradient(135deg,#b9b0a8,#5a3a2e 50%,#8a5a48)"></div>
</div></div>

<h2 class="section-title abs" style="top:1622px">Latest Blog</h2>
<article class="blog-card abs" style="left:80px;top:1702px">
  <div class="blog-photo" role="img" aria-label="Photo of a chocolate dessert in a white cup" style="background:linear-gradient(135deg,#d9cfc4,#5a2e22 55%,#8a4a3a)"></div>
  <div class="blog-body">
    <h3>Lorem Ipsum is simply dummy text of the printing.</h3>
    <div class="blog-date"><svg width="13" height="13" viewBox="0 0 13 13"><rect x="1" y="2" width="11" height="10" fill="none" stroke="#555"/><path d="M1 5h11M4 0v3M9 0v3" stroke="#555"/></svg>12th April 2017</div>
    <p>Lorem Ipsum is simply dummy text of the printing.</p>
  </div>
</article>
<article class="blog-card abs" style="left:642px;top:1702px">
  <div class="blog-photo" role="img" aria-label="Photo of a bowl of bean and vegetable salad" style="background:linear-gradient(135deg,#e8e4dc,#b84a2a 50%,#2a3a5a)"></div>
  <div class="blog-body">
    <h3>Lorem Ipsum is simply dummy text of the printing.</h3>
    <div class="blog-date"><svg width="13" height="13" viewBox="0 0 13 13"><rect x="1" y="2" width="11" height="10" fill="none" stroke="#555"/><path d="M1 5h11M4 0v3M9 0v3" stroke="#555"/></svg>12th April 2017</div>
    <p>Lorem Ipsum is simply dummy text of the printing.</p>
  </div>
</article>

<section class="contact abs"></section>
<div class="contact-photo abs" role="img" aria-label="Photo of cocoa-dusted chocolate balls with pomegranate seeds in a white bowl"></div>
<div class="contact-card abs">
  <h2>Contact Info</h2>
  <div class="c-brand">varbek</div>
  <p class="c-tag">Fuel for the Daily Trail-SeekerTM</p>
  <p class="c-phone">Call Us : 0400 555 918</p>
  <p class="c-mail">email us : hello@varbekfoods.example</p>
</div>

<footer class="site-footer abs">
  <div class="footer-links"><span>Delievery Information</span><span>Privacy Policy</span><span>Sitemap</span><span>Contact Us</span></div>
  <div class="footer-social"><span></span><span></span><span></span></div>
  <div class="copyright">©varbek. 2017 - All Rights Reserved.</div>
</footer>

</body>
</html>
```